Brightloom Business Card/Stationary
Marketing Co. Web/SEO
Brightloom Business Card/Stationary - Marketing
Creative Brief
Use specific fonts
Do your thing, logo is Trajan Pro and Tunga
Bright & Fun-filled
Reginald T. Ostrander
Senior SEO Consultant
www.brightloomxq.example
555-0142 (LOOM)
555-0187 (LOOM)
reggie@brightloomxq.example
I want this to be creative and memorable. We do web design, development and SEO. Make us stand out! I need business cards, stationary and envelop concepts.
I would like the back of the card to be the black logo with a corner peeled back slightly to reveal html code (to suggest what we do with website coding). If you don't know what that looks like right click a website and select view page source to get an idea.

```html
<!DOCTYPE html>
<html lang="en">
<head>
<meta charset="utf-8">
<title>Brightloom Stationery Set</title>
<link href="https://fonts.googleapis.com/css2?family=Cinzel:wght@600&family=Lato:wght@400;700&display=swap" rel="stylesheet">
<style>
:root{
  --backdrop:#d8d3ce;
  --paper:#ffffff;
  --ink-dark:#0d1620;
  --navy:#0a2a4a;
  --blue:#1a6fb5;
  --blue-bright:#3aa0e6;
  --contact-light:#dbeaf7;
  --faint:#e4e8ec;
}
*{margin:0;padding:0;box-sizing:border-box}
html,body{width:1200px;height:434px;overflow:hidden}
body{background:var(--backdrop);position:relative;font-family:"Lato",sans-serif}
.piece{position:absolute;overflow:hidden;box-shadow:0 2px 6px rgba(0,0,0,.25)}
.piece svg.art{position:absolute;inset:0;width:100%;height:100%}
.brand{position:absolute;display:flex;align-items:center;gap:4px;font-family:"Cinzel",serif;font-weight:600;color:var(--navy);white-space:nowrap}
.brand .dot{border-radius:50%;background:var(--blue);flex:none}
.brand.light{color:#fff}

.card{width:120px;height:66px;top:24px;background:var(--ink-dark)}
.card-front{left:86px}
.card-back{left:212px}
.card .brand{font-size:7px}
.card-front .brand{left:8px;top:8px}
.card-front .brand .dot{width:9px;height:9px}
.card .person{position:absolute;left:8px;bottom:9px;color:#fff;font-size:5px;line-height:1.4;white-space:nowrap}
.card .person strong{font-size:6px;display:block}
.card-back .brand{left:8px;top:8px}
.card-back .brand .dot{width:9px;height:9px}
.card-back .contact{position:absolute;left:8px;bottom:8px;color:var(--contact-light);font-size:4.5px;line-height:1.5;white-space:nowrap}

.envelope{width:286px;height:118px;left:38px;background:var(--paper)}
.envelope-back{top:96px}
.envelope-front{top:240px}
.envelope-back .brand{left:50%;top:40px;transform:translateX(-50%)}
.envelope-back .brand .dot{width:12px;height:12px;border:2px solid #fff}
.envelope-front .brand{left:10px;top:10px;font-size:7px}
.envelope-front .brand .dot{width:14px;height:14px}
.envelope-front .seal{position:absolute;right:70px;top:22px;width:60px;height:60px;border-radius:50%;background:var(--faint)}

.letterhead{top:46px;width:232px;height:326px;background:var(--paper)}
.lh-one{left:384px}
.lh-two{left:646px;top:40px;height:332px}
.lh-three{left:900px;width:228px}
.letterhead .brand{left:14px;top:14px;font-size:7px}
.letterhead .brand .dot{width:14px;height:14px}
.letterhead .seal{position:absolute;left:50%;top:92px;transform:translateX(-50%);width:74px;height:74px;border-radius:50%;background:var(--faint)}
.letterhead .contact{position:absolute;right:30px;bottom:9px;color:var(--contact-light);font-size:4.5px;line-height:1.6;white-space:nowrap}
</style>
</head>
<body>

<div class="piece card card-front">
  <svg class="art" viewBox="0 0 120 66" preserveAspectRatio="none" aria-hidden="true">
    <defs><linearGradient id="cardBlue" x1="0" x2="1"><stop offset="0" stop-color="#0a2a4a"/><stop offset="1" stop-color="#3aa0e6"/></linearGradient></defs>
    <path d="M0 40 C40 30 80 52 120 36 L120 66 L0 66Z" fill="url(#cardBlue)" opacity=".55"/>
  </svg>
  <div class="brand light"><span class="dot"></span>Brightloom</div>
  <div class="person"><strong>Reginald T. Ostrander</strong>Senior SEO Consultant</div>
</div>

<div class="piece card card-back">
  <svg class="art" viewBox="0 0 120 66" preserveAspectRatio="none" aria-hidden="true">
    <path d="M0 50 C40 44 80 60 120 46 L120 66 L0 66Z" fill="#1a6fb5" opacity=".6"/>
  </svg>
  <div class="brand light"><span class="dot"></span>Brightloom</div>
  <div class="contact">www.brightloomxq.example<br>555-0142 (LOOM)<br>reggie@brightloomxq.example</div>
</div>

<div class="piece envelope envelope-back">
  <svg class="art" viewBox="0 0 286 118" preserveAspectRatio="none" aria-hidden="true">
    <defs><linearGradient id="flapBlue" x1="0" x2="1"><stop offset="0" stop-color="#0a2a4a"/><stop offset=".5" stop-color="#3aa0e6"/><stop offset="1" stop-color="#0a2a4a"/></linearGradient></defs>
    <path d="M0 0 L286 0 L286 8 L143 54 L0 8Z" fill="url(#flapBlue)"/>
    <path d="M0 0 L286 0 L286 4 L143 46 L0 4Z" fill="#0d1620"/>
  </svg>
  <div class="brand"><span class="dot"></span></div>
</div>

<div class="piece envelope envelope-front">
  <svg class="art" viewBox="0 0 286 118" preserveAspectRatio="none" aria-hidden="true">
    <defs><linearGradient id="envBlue" x1="0" x2="1"><stop offset="0" stop-color="#0a2a4a"/><stop offset="1" stop-color="#3aa0e6"/></linearGradient></defs>
    <path d="M0 100 C90 88 190 118 286 92 L286 118 L0 118Z" fill="url(#envBlue)"/>
    <path d="M0 97 C90 85 190 115 286 89" fill="none" stroke="#0d1620" stroke-width="2"/>
  </svg>
  <div class="seal"></div>
  <div class="brand"><span class="dot"></span>Brightloom</div>
</div>

<div class="piece letterhead lh-one">
  <svg class="art" viewBox="0 0 232 326" preserveAspectRatio="none" aria-hidden="true">
    <defs><linearGradient id="lhBlue" x1="0" x2="1"><stop offset="0" stop-color="#0a2a4a"/><stop offset=".6" stop-color="#1a6fb5"/><stop offset="1" stop-color="#3aa0e6"/></linearGradient></defs>
    <path d="M0 290 C70 276 150 312 232 284 L232 326 L0 326Z" fill="url(#lhBlue)"/>
    <path d="M0 286 C70 272 150 308 232 280" fill="none" stroke="#0d1620" stroke-width="2"/>
  </svg>
  <div class="brand"><span class="dot"></span>Brightloom</div>
  <div class="seal"></div>
  <div class="contact">www.brightloomxq.example<br>555-0142 (LOOM)<br>reggie@brightloomxq.example</div>
</div>

<div class="piece letterhead lh-two">
  <svg class="art" viewBox="0 0 232 332" preserveAspectRatio="none" aria-hidden="true">
    <defs><linearGradient id="lhBlue2" x1="1" x2="0"><stop offset="0" stop-color="#0a2a4a"/><stop offset=".6" stop-color="#1a6fb5"/><stop offset="1" stop-color="#3aa0e6"/></linearGradient></defs>
    <path d="M0 292 C80 310 160 276 232 296 L232 332 L0 332Z" fill="url(#lhBlue2)"/>
    <path d="M0 288 C80 306 160 272 232 292" fill="none" stroke="#0d1620" stroke-width="2"/>
  </svg>
  <div class="brand"><span class="dot"></span>Brightloom</div>
  <div class="seal"></div>
  <div class="contact">www.brightloomxq.example<br>555-0187 (LOOM)<br>reggie@brightloomxq.example</div>
</div>

<div class="piece letterhead lh-three">
  <svg class="art" viewBox="0 0 228 326" preserveAspectRatio="none" aria-hidden="true">
    <defs><linearGradient id="lhBlue3" x1="0" x2="1"><stop offset="0" stop-color="#0a2a4a"/><stop offset="1" stop-color="#3aa0e6"/></linearGradient></defs>
    <path d="M0 298 C70 286 150 316 228 292 L228 326 L0 326Z" fill="url(#lhBlue3)"/>
    <path d="M0 294 C70 282 150 312 228 288" fill="none" stroke="#0d1620" stroke-width="2"/>
  </svg>
  <div class="brand"><span class="dot"></span>Brightloom</div>
  <div class="seal"></div>
</div>

</body>
</html>
```